TALVORIA Lunch and Learn Presentation

We are hosting a live lunch and learn and need to create a presentation for our company. Here is an outline of what is needed and I want to have someone use our new brand logo, colors, and fonts to create an engaging presentation.
Here is the outline.
3. Copy, Layout & Directions for Each Slide
Slide 1: Title
Background: Blue gradient (top left to bottom right) or a subtle tech pattern
Header:
TALVORIA Lunch & Learn
Subtext:
Smarter business communication starts here
Details (bottom):
September 1, 2025 | Zarn Offices
Logo Placeholder: Centered above or below the title (add after your logo file is available)
Design Tip: Keep plenty of whitespace. Use white or light grey for text.
Slide 2: Who We Are
Layout: Split screen.
Left: “Formerly TeLVORIA” with old logo placeholder
Right: “Now TALVORIA” with new logo placeholder
Below: Timeline or row of company milestones
Key Points (bullets):
Local expertise with national reach
Over [X] years helping businesses stay connected
Rebranded from TeLVORIA → TALVORIA for clarity, growth, and innovation
Visual: Leave space for graphics or timeline (add later)
Slide 3: Why the Rebrand?
Background: Subtle grey tech pattern or white
Big Visual:
Word cloud or three large, bold text words across the slide:
Clarity | Innovation | Future-Ready
Bullets:
To eliminate confusion in the market
To reflect our expanded solutions & AI innovation
To position our partners and customers for the future
Slide 4: Our Mission
Background: White with blue accent bar at top/bottom
Mission Statement (big/bold):
“Helping businesses never miss a call and improving how people connect.”
Key Points (bullets):
Reliable communications made simple
Technology + human-first service
Tools that free up people to do what they do best
Placeholder: For a photo (collaborating team, handshake, etc.)
Slide 5: Platform Overview
Header:
TALVORIA Loomra
Icons: Row/circle with: Phone | Text bubble | Globe/portal | Support team
Features (bullets):
Business-class phone system
Core calling features + voicemail
Business texting & mobility
Easy-to-manage web portal
Backed by our support team
Design Tip: Use blue for icons, grey for text
Slide 6: Key Differentiators
Layout: 2-column comparison table
Left: TALVORIA (Blue background, white text, checkmarks)
Right: National Carriers (Grey or white background, minimal checkmarks)
Bullets:
Local support, national scalability
Flexible solutions (not one-size-fits-all)
AI-powered features (Brevida)
Transparent pricing & partner-first approach
Slide 7: Demo Flow
Header:
How Loomra Works in Action
Diagram:
Icons in horizontal order:
[Phone] → [AI/robot] → [Staff] → [Dashboard]
Steps:
Customer calls/texts in
Brevida AI Receptionist answers (if enabled)
FAQs / scheduling handled automatically
Human team picks up higher-value conversations
Everything tracked in one platform
Slide 8: Spotlight: Brevida AI Receptionist
Layout: Side-by-side (two columns)
Left: “Without Brevida” (small icons for missed calls, stressed staff)
Right: “With Brevida” (happy customers, productive staff)
Key Features (bullets):
Answers calls 24/7
Handles FAQs instantly
Schedules appointments
Frees staff to focus on relationships
Key Message:
Brevida = your first line of support, not a replacement for people
Slide 9: Customer Story / Use Case
Header:
Example: HVAC Service Company
Layout: Split screen
Left: “Before” (chaotic image/placeholder), bullets:
Missed after-hours calls
Overwhelmed front desk
Right: “After” (organized image/placeholder), bullets:
Brevida handled 60% of inbound calls
No missed opportunities
Staff had time for complex customer needs
Slide 10: Partner & Customer Benefits
Header:
Key Benefits
Checklist with icons (row or column):
Never miss a call or opportunity
Improve customer satisfaction & retention
Boost staff productivity
Gain a competitive edge with AI-powered communications
Dedicated local support team
Design Tip: Use blue/grey icons, white background
Slide 11: What’s Next?
Header:
What’s Next?
Bullets (with icons):
Try Brevida AI Receptionist free trial
Explore Loomra for smarter calling
Partner with TALVORIA for growth opportunities
CTA Visual:
Bold blue rectangle/banner with white CTA text (Try Now, Explore, Partner)
Slide 12: Thank You / Q&A
Header:
Questions?
Subtext:
Let’s talk about how TALVORIA can help your business never miss a call.
Footer:
TALVORIA Logo (placeholder)
Contact: info@gettalvoria.com
Website: www.gettalvoria.com
Background: Blue or white, with blue text

```html
<!DOCTYPE html>
<html lang="en">
<head>
<meta charset="utf-8">
<title>TALVORIA Lunch &amp; Learn – Slide Set</title>
<link rel="stylesheet" href="https://fonts.googleapis.com/css2?family=Montserrat:wght@400;500;600;700&display=swap">
<style>
  :root{
    --board:#02355a;
    --blue:#0d96ee;
    --blue-light:#1fa2f3;
    --blue-deep:#0a56a6;
    --navy:#123a66;
    --ink:#2b2f36;
    --muted:#d2d5d9;
    --panel-grey:#f3f3f3;
    --white:#ffffff;
  }
  *{margin:0;padding:0;box-sizing:border-box}
  html,body{width:1200px;height:1001px;overflow:hidden;background:var(--board)}
  body{position:relative;font-family:"Montserrat",Arial,sans-serif;color:var(--ink)}
  .slide{position:absolute;width:467px;height:262px;background:var(--white);overflow:hidden}
  .slide--title{left:119px;top:74px;background:linear-gradient(135deg,var(--blue-light) 0%,var(--blue) 100%);color:var(--white)}
  .slide--who{left:613px;top:74px}
  .slide--why{left:119px;top:368px}
  .slide--mission{left:613px;top:368px}
  .slide--platform{left:119px;top:664px}
  .abs{position:absolute}

  /* title slide */
  .title__brand{left:43px;top:62px;font-size:22px;font-weight:700;letter-spacing:.5px}
  .title__main{left:41px;top:88px;font-size:44px;font-weight:500;line-height:39px}
  .title__sub{left:43px;top:174px;font-size:7px;font-weight:500}
  .title__date{left:43px;top:225px;font-size:7.5px;font-weight:500}

  /* heading */
  .slide-heading{left:0;width:100%;text-align:center;color:var(--blue);font-weight:700;font-size:19px}

  /* who */
  .split{left:18px;top:64px;width:433px;height:99px;display:flex}
  .split__half{flex:1;position:relative;text-align:center;font-size:8.4px;font-weight:500;padding-top:19px;line-height:10.5px}
  .split__half--old{background:var(--panel-grey);color:var(--blue-deep)}
  .split__half--new{background:var(--blue);color:var(--white)}
  .logo-slot{position:absolute;left:43px;top:50px;width:130px;height:32px}
  .logo-slot--old{background:var(--white);border:2px solid #c4c4c4}
  .logo-slot--new{background:var(--white);border:2px solid var(--navy);display:flex;align-items:center;justify-content:center;
    font-size:15px;font-weight:500;letter-spacing:2.5px;color:#4d6a8a}
  .who__points{left:247px;top:189px;list-style:none;font-size:7.8px;line-height:9.6px;color:var(--blue-deep);font-weight:500}

  /* why */
  .cloud span{position:absolute;line-height:1;white-space:nowrap;color:var(--muted);font-weight:500}
  .cloud .key{color:var(--blue);font-weight:700}
  .why__reasons{left:0;width:100%;top:239px;text-align:center;font-size:5.8px;color:var(--blue-deep);font-weight:500}

  /* mission */
  .mission__photo{right:0;top:0;width:300px;height:262px;
    background:linear-gradient(100deg,rgba(255,255,255,0) 0%,rgba(215,229,246,.55) 28%,rgba(143,179,227,.85) 55%,#2c5a9c 82%,#1b3f7a 100%)}
  .mission__title{left:39px;top:63px;font-size:24px;font-weight:700;color:var(--blue)}
  .mission__statement{left:39px;top:95px;width:180px;font-size:7.3px;line-height:9.6px;color:var(--ink)}
  .feature{position:absolute;font-size:7.5px;color:var(--ink);white-space:nowrap}
  .feature::after{content:"";position:absolute;left:0;top:12px;width:32px;height:2.5px;background:var(--blue)}

  /* platform */
  .platform__brand{left:349px;top:24px;font-size:13px;font-weight:500;letter-spacing:1.8px;color:#3f5c7c}
  .platform__title{left:47px;top:45px;font-size:24px;line-height:25px;color:var(--blue)}
  .platform__title b{font-weight:700;display:block}
  .platform__title span{font-weight:500}
  .icon-tile{position:absolute;top:113px;width:47px;height:47px;background:var(--blue);display:flex;align-items:center;justify-content:center}
  .icon-tile svg{width:28px;height:28px}
</style>
</head>
<body>

<!-- Slide 1: Title -->
<section class="slide slide--title">
  <div class="abs title__brand">TALVORIA</div>
  <div class="abs title__main">Lunch<br>&amp; Learn</div>
  <div class="abs title__sub">Smarter business communication starts here</div>
  <div class="abs title__date">September 1, 2025 | Zarn Offices</div>
</section>

<!-- Slide 2: Who We Are -->
<section class="slide slide--who">
  <h2 class="abs slide-heading" style="top:34px">Who We Are</h2>
  <div class="abs split">
    <div class="split__half split__half--old">Formerly<br>TeLVORIA
      <div class="logo-slot logo-slot--old"></div>
    </div>
    <div class="split__half split__half--new">Now<br>TALVORIA
      <div class="logo-slot logo-slot--new">TALVORIA</div>
    </div>
  </div>
  <svg class="abs" style="left:220px;top:116px" width="28" height="28" viewBox="0 0 28 28">
    <circle cx="14" cy="14" r="14" fill="#ffffff"/>
    <path d="M11 8 L17 14 L11 20" stroke="#123a66" stroke-width="3" fill="none" stroke-linecap="round" stroke-linejoin="round"/>
  </svg>
  <svg class="abs" style="left:0;top:170px" width="240" height="92" viewBox="0 0 240 92">
    <rect x="26" y="7" width="20" height="13" rx="1.5" fill="none" stroke="#0d96ee" stroke-width="1.6"/>
    <rect x="29" y="10" width="14" height="7" fill="#0d96ee"/>
    <path d="M33 20 v3 h6 v-3 M31 24 h10" stroke="#0d96ee" stroke-width="1.5" fill="none"/>
    <line x1="18" y1="32" x2="231" y2="32" stroke="#123a66" stroke-width="1.2"/>
    <g fill="#ffffff" stroke="#123a66" stroke-width="1.3">
      <circle cx="37" cy="32" r="4"/><circle cx="70" cy="32" r="4"/>
      <circle cx="106" cy="32" r="4"/><circle cx="139" cy="32" r="4"/>
      <circle cx="172" cy="32" r="4"/><circle cx="205" cy="32" r="4"/>
    </g>
    <circle cx="106" cy="32" r="2" fill="#123a66"/>
    <rect x="86" y="49" width="36" height="21" rx="2.5" fill="#0d96ee"/>
    <path d="M101 49 L104 45 L107 49 Z" fill="#0d96ee"/>
  </svg>
  <ul class="abs who__points">
    <li>• Local expertise with national reach</li>
    <li>• Over [X] years helping businesses stay connected</li>
    <li>• Rebranded from TeLVORIA</li>
    <li>• TALVORIA for clarity, growth, innovation</li>
  </ul>
</section>

<!-- Slide 3: Why the Rebrand? -->
<section class="slide slide--why">
  <h2 class="abs slide-heading" style="top:34px">Why the Rebrand?</h2>
  <div class="cloud">
    <span style="left:158px;top:74px;font-size:9.5px">technology</span>
    <span style="left:229px;top:78px;font-size:8.5px">resilience</span>
    <span class="key" style="left:167px;top:87px;font-size:20px">Clarity</span>
    <span style="left:241px;top:94px;font-size:10.5px">creativity</span>
    <span style="left:120px;top:106px;font-size:9.5px">originality</span>
    <span class="key" style="left:175px;top:106px;font-size:31px">Innovation</span>
    <span style="left:106px;top:120px;font-size:14px">progress</span>
    <span class="key" style="left:114px;top:138px;font-size:23px">Future-Ready</span>
    <span style="left:290px;top:143px;font-size:9.5px">evolution</span>
    <span style="left:281px;top:155px;font-size:15px">disruption</span>
    <span style="left:135px;top:161px;font-size:11px">sustainability</span>
    <span style="left:214px;top:172px;font-size:11px">anticipation</span>
    <span style="left:153px;top:178px;font-size:7px">preparation</span>
    <span style="left:178px;top:188px;font-size:13px">foresight</span>
    <span style="left:243px;top:190px;font-size:20px">growth</span>
  </div>
  <p class="abs why__reasons">• Eliminate confusion in the market • Reflect expanded solutions &amp; AI innovation • Position partners/customers for the future</p>
</section>

<!-- Slide 4: Our Mission -->
<section class="slide slide--mission">
  <div class="abs mission__photo" role="img" aria-label="Photo placeholder: two business people shaking hands"></div>
  <h2 class="abs mission__title">Our Mission</h2>
  <p class="abs mission__statement">Helping businesses never miss a call and improving how people connect.</p>
  <div class="feature" style="left:39px;top:148px">Reliable communications made simple</div>
  <div class="feature" style="left:39px;top:173px">Technology + human-first service</div>
  <div class="feature" style="left:39px;top:198px">Tools that free people to do what they do best</div>
</section>

<!-- Slide 5: Platform Overview -->
<section class="slide slide--platform">
  <div class="abs platform__brand">TALVORIA</div>
  <h2 class="abs platform__title"><b>TALVORIA</b><span>Loomra</span></h2>

  <div class="icon-tile" style="left:48px" aria-label="Phone">
    <svg viewBox="0 0 24 24"><path fill="#fff" d="M6.6 10.8a15.1 15.1 0 0 0 6.6 6.6l2.2-2.2c.3-.3.7-.4 1-.2 1.1.4 2.3.6 3.6.6.6 0 1 .4 1 1V20c0 .6-.4 1-1 1A17 17 0 0 1 3 4c0-.6.4-1 1-1h3.5c.6 0 1 .4 1 1 0 1.3.2 2.5.6 3.6.1.3 0 .7-.2 1z"/></svg>
  </div>
  <div class="icon-tile" style="left:112px" aria-label="Text message">
    <svg viewBox="0 0 24 24"><path fill="#fff" d="M4 4h16a2 2 0 0 1 2 2v9a2 2 0 0 1-2 2h-9l-5 4v-4H4a2 2 0 0 1-2-2V6a2 2 0 0 1 2-2z"/></svg>
  </div>
  <div class="icon-tile" style="left:171px" aria-label="Web portal">
    <svg viewBox="0 0 24 24" fill="none" stroke="#fff" stroke-width="1.6"><circle cx="12" cy="12" r="9.5"/><ellipse cx="12" cy="12" rx="4.2" ry="9.5"/><line x1="2.5" y1="12" x2="21.5" y2="12"/><line x1="12" y1="2.5" x2="12" y2="21.5"/><path d="M4.5 7h15M4.5 17h15"/></svg>
  </div>
  <div class="icon-tile" style="left:235px" aria-label="Support team">
    <svg viewBox="0 0 24 24" fill="#fff"><circle cx="12" cy="8" r="3"/><circle cx="5.5" cy="10" r="2.3"/><circle cx="18.5" cy="10" r="2.3"/><path d="M6.5 19c0-3.3 2.5-6 5.5-6s5.5 2.7 5.5 6z"/><path d="M1 19c0-2.6 1.9-4.7 4.2-4.7 1 0 1.4.2 1.9.5A7 7 0 0 0 5.3 19z"/><path d="M23 19c0-2.6-1.9-4.7-4.2-4.7-1 0-1.4.2-1.9.5a7 7 0 0 1 1.8 4.2z"/></svg>
  </div>

  <div class="feature" style="left:47px;top:177px">Business-class phone system</div>
  <div class="feature" style="left:47px;top:198px">Core calling features + voicemail</div>
  <div class="feature" style="left:47px;top:219px">Business texting &amp; mobility</div>
  <div class="feature" style="left:190px;top:177px">Easy-to-manage web portal</div>
  <div class="feature" style="left:190px;top:198px">Backed by support team</div>
</section>

</body>
</html>
```